RT Pemberly Electric Yard Sign

Looking to have a yard sign designed that we can place at projects we are working on. Most likely will be 18" H x 24" W but flexible that we can increase the size if necessary. It should include our logo, our phone # 609-555-0147, website rtpemberlyelectric-example.com and slogan, built on integrity, driven by excellence. Colors should match our brand.

```html
<!DOCTYPE html>
<html lang="en">
<head>
<meta charset="UTF-8">
<title>RT Pemberly Electric Yard Sign</title>
<link href="https://fonts.googleapis.com/css2?family=Michroma&family=Saira:wght@700;800&display=swap" rel="stylesheet">
<style>
  :root {
    --navy: #2a3558;
    --red: #e21f2c;
    --white: #ffffff;
    --ink: #1c1f2a;
    --backdrop: #f1f1ef;
  }
  * { margin: 0; padding: 0; box-sizing: border-box; }
  html, body {
    width: 1200px;
    height: 411px;
    overflow: hidden;
    background: var(--backdrop);
  }
  .canvas {
    width: 1200px;
    height: 411px;
    display: flex;
    align-items: center;
    justify-content: center;
  }
  .yard-sign {
    position: relative;
    width: 500px;
    height: 374px;
    background: var(--white);
    box-shadow: 0 6px 18px rgba(0,0,0,0.15);
    overflow: hidden;
  }
  .brand-row {
    position: absolute;
    top: 72px;
    left: 0;
    width: 100%;
    display: flex;
    align-items: center;
    justify-content: center;
    gap: 12px;
  }
  .brand-dot {
    width: 18px;
    height: 18px;
    border-radius: 50%;
    background: var(--red);
  }
  .brand-name {
    font-family: "Michroma", sans-serif;
    font-size: 23px;
    color: var(--red);
    text-transform: uppercase;
    letter-spacing: 1px;
    white-space: nowrap;
  }
  .trade-line {
    position: absolute;
    top: 146px;
    left: 0;
    width: 100%;
    text-align: center;
    font-family: "Michroma", sans-serif;
    font-size: 17px;
    letter-spacing: 4px;
    color: var(--navy);
  }
  .rule {
    position: absolute;
    left: 24px;
    width: 452px;
    height: 3px;
    background: var(--red);
  }
  .rule-top { top: 180px; }
  .slogan {
    position: absolute;
    top: 193px;
    left: 0;
    width: 100%;
    text-align: center;
    font-family: "Saira", sans-serif;
    font-weight: 700;
    font-size: 19px;
    color: var(--ink);
    letter-spacing: 0.6px;
  }
  .slogan em { font-style: normal; color: var(--red); }
  .contact-band {
    position: absolute;
    top: 236px;
    left: 0;
    width: 100%;
    height: 138px;
    background: var(--navy);
  }
  .rule-band-top { top: 15px; left: 33px; width: 434px; }
  .rule-band-bottom { top: 122px; left: 33px; width: 434px; }
  .phone {
    position: absolute;
    top: 18px;
    left: 0;
    width: 100%;
    text-align: center;
    font-family: "Saira", sans-serif;
    font-weight: 800;
    font-size: 58px;
    line-height: 70px;
    color: var(--white);
    letter-spacing: 1px;
  }
  .website {
    position: absolute;
    top: 91px;
    left: 0;
    width: 100%;
    text-align: center;
    font-family: "Saira", sans-serif;
    font-weight: 700;
    font-size: 15px;
    color: var(--white);
    letter-spacing: 3.4px;
  }
</style>
</head>
<body>
  <main class="canvas">
    <section class="yard-sign" aria-label="RT Pemberly Electric yard sign">
      <div class="brand-row">
        <span class="brand-dot"></span>
        <span class="brand-name">RT Pemberly Electric</span>
      </div>
      <p class="trade-line">Electrical Contractor</p>
      <div class="rule rule-top"></div>
      <p class="slogan">built on <em>integrity</em>, driven by <em>excellence.</em></p>
      <div class="contact-band">
        <div class="rule rule-band-top"></div>
        <p class="phone">609-555-0147</p>
        <p class="website">www.rtpemberlyelectric-example.com</p>
        <div class="rule rule-band-bottom"></div>
      </div>
    </section>
  </main>
</body>
</html>
```